Annual Event PPT Template

We need a PowerPoint template to use for a big annual event we host. Attached is the logo we use for everything. You can also reference our website (listed below) and our letterhead for design inspiration.

Please be sure to include our contact information on all of the PPT slides:
1. Phone: 802-417-3926
2. Address: 342 Fernwick Hollow Road, Williston, VT 05482
3. Website: www.QuarvelSys.com

```html
<!DOCTYPE html>
<html lang="en">
<head>
<meta charset="utf-8">
<title>Annual Event Slide Template</title>
<link rel="stylesheet" href="https://fonts.googleapis.com/css2?family=Merriweather:wght@700&family=Montserrat:wght@400&display=swap">
<style>
  :root {
    --brand-navy: #235a86;
    --footer-text: #5f8db9;
    --band-light: #f4f4f5;
    --band-grey: #dcdee1;
    --stage-deep: #6e9ac0;
    --stage-mid: #9fbbd3;
    --stage-pale: #d2dde7;
    --visual-blue: #2f6fc0;
    --visual-cyan: #1fa3df;
  }
  * { margin: 0; padding: 0; box-sizing: border-box; }
  html, body { width: 1200px; height: 675px; overflow: hidden; background: #ffffff; }
  .slide {
    position: relative;
    width: 1200px;
    height: 675px;
    overflow: hidden;
    background: var(--band-light);
  }
  .header-band {
    position: absolute;
    left: 0; top: 0;
    width: 1200px; height: 118px;
    background: linear-gradient(90deg, var(--band-grey) 0%, #eeeff0 30%, #f7f7f8 55%, #f7f7f8 100%);
  }
  .content-stage {
    position: absolute;
    left: 0; top: 118px;
    width: 1200px; height: 510px;
    background: linear-gradient(90deg, var(--stage-deep) 0%, var(--stage-mid) 25%, #c3d2df 40%, var(--stage-pale) 52%, #cfdae5 62%, #bccdde 75%, #aec4da 100%);
  }
  .hero-visual {
    position: absolute;
    right: 0; top: 0;
    width: 620px; height: 628px;
    background:
      radial-gradient(ellipse at 85% 60%, var(--visual-cyan) 0%, rgba(31,163,223,0) 55%),
      linear-gradient(90deg, rgba(47,111,192,0) 0%, rgba(47,111,192,0.55) 30%, var(--visual-blue) 55%, #2a7fcf 80%, var(--visual-cyan) 100%);
    -webkit-mask-image: linear-gradient(90deg, transparent 0%, #000 35%), linear-gradient(180deg, #000 70%, transparent 100%);
    -webkit-mask-composite: source-in;
    mask-image: linear-gradient(90deg, transparent 0%, #000 35%);
  }
  .footer-band {
    position: absolute;
    left: 0; top: 628px;
    width: 1200px; height: 47px;
    background: linear-gradient(90deg, var(--band-grey) 0%, #eceeef 40%, #e9ebee 100%);
    display: flex;
    align-items: center;
    justify-content: center;
  }
  .contact-line {
    font-family: 'Montserrat', sans-serif;
    font-weight: 400;
    font-size: 16.5px;
    color: var(--footer-text);
    letter-spacing: 0.2px;
    margin-left: 20px;
    white-space: nowrap;
  }
  .brand-name {
    position: absolute;
    left: 70px; top: 28px;
    font-family: 'Merriweather', serif;
    font-weight: 700;
    font-size: 40px;
    line-height: 1;
    color: var(--brand-navy);
    letter-spacing: -0.5px;
  }
</style>
</head>
<body>
  <div class="slide">
    <div class="header-band"></div>
    <div class="content-stage"></div>
    <div class="hero-visual" role="img" aria-label="Businessman in a blue suit holding a tablet, overlaid with a translucent world map"></div>
    <div class="brand-name">QuarvelSys</div>
    <div class="footer-band">
      <p class="contact-line">802-417-3926 | 342 Fernwick Hollow Road, Williston, VT 05482 | www.QuarvelSys.com</p>
    </div>
  </div>
</body>
</html>
```